Service business needs Business Card Design

Looking to create a new business card design that is both professional and unique the can highlight the many services we offer throughout the seasons. Our tagline is "The Steadfast Touch"
Licensed & Insured: PA392617 has to be small and on the back side of the card.
On the Front:
FirstName LastName
Title
We offer the following services:
Deck Repair and Maintenance
Deck Cleaning and Staining/Painting
Power Washing/House Washing
Landscape Lighting Installation
Christmas Lighting Installation

```html
<!DOCTYPE html>
<html lang="en">
<head>
<meta charset="utf-8">
<title>Clearway Services – Business Card</title>
<link rel="stylesheet" href="https://fonts.googleapis.com/css2?family=Arimo:ital,wght@0,400;0,700;1,700&display=swap">
<style>
  :root {
    --bg: #e4e4e2;
    --navy: #0a4e93;
    --navy-deep: #073f7a;
    --navy-soft: #155d9f;
    --sky: #4cb6ea;
    --white: #ffffff;
    --ink-faint: #0c3f74;
  }
  * { margin: 0; padding: 0; box-sizing: border-box; }
  html, body { width: 1200px; height: 801px; overflow: hidden; }
  body {
    background: var(--bg);
    font-family: "Arimo", Arial, sans-serif;
    position: relative;
  }
  .card {
    position: absolute;
    top: 246px;
    width: 540px;
    height: 309px;
    background: var(--navy);
    color: var(--white);
    overflow: hidden;
    box-shadow: 0 6px 18px rgba(0,0,0,.22);
  }
  .card--front { left: 40px; }
  .card--back  { left: 620px; }

  /* front */
  .front__rays {
    position: absolute;
    right: 0; top: 0;
    width: 300px; height: 290px;
    background: radial-gradient(ellipse at 85% 10%, var(--navy-soft) 0%, var(--navy-soft) 45%, rgba(21,93,159,0) 75%);
  }
  .front__edge {
    position: absolute; left: 0; right: 0; bottom: 0; height: 9px;
    display: flex;
  }
  .front__edge-white { width: 52%; background: var(--white); }
  .front__edge-sky { flex: 1; background: var(--sky); }
  .brand-name {
    position: absolute; left: 30px; top: 52px;
    font-size: 30px; font-weight: 700; letter-spacing: 2px;
    color: var(--white);
    line-height: 1;
  }
  .brand-name__sub {
    display: block; font-size: 13px; letter-spacing: 9px; margin-top: 6px;
  }
  .person { position: absolute; left: 30px; top: 140px; }
  .person__name { font-size: 17px; font-weight: 700; letter-spacing: .5px; }
  .person__title { font-size: 14px; margin-top: 3px; }
  .contacts { position: absolute; left: 30px; top: 200px; list-style: none; }
  .contacts li {
    display: flex; align-items: center; gap: 8px;
    font-size: 14px; line-height: 22px;
  }
  .contacts svg { width: 13px; height: 13px; flex: none; }
  .address {
    position: absolute; right: 30px; bottom: 26px;
    text-align: right; font-size: 13px; line-height: 16px;
  }

  /* back */
  .back__brand {
    position: absolute; left: 0; right: 0; top: 48px;
    text-align: center;
    font-size: 34px; font-weight: 700; letter-spacing: 3px;
    color: var(--ink-faint);
    line-height: 1;
  }
  .back__brand span { display: block; font-size: 14px; letter-spacing: 12px; margin-top: 6px; }
  .back__license {
    position: absolute; left: 0; right: 0; top: 124px;
    text-align: center; font-size: 13px;
  }
  .services {
    position: absolute; left: 0; right: 0; top: 148px;
    text-align: center; font-size: 14px; line-height: 19px;
  }
  .services__lead { font-weight: 700; font-size: 15px; }
  .tagline-band {
    position: absolute; left: 0; right: 0; top: 240px; height: 26px;
    background: linear-gradient(90deg, rgba(76,182,234,0) 0%, var(--sky) 45%, var(--sky) 65%, rgba(76,182,234,0) 100%);
  }
  .tagline {
    position: absolute; left: 0; right: 0; top: 244px;
    text-align: center; font-size: 16px; font-weight: 700; font-style: italic;
    color: var(--navy-deep);
  }
</style>
</head>
<body>

<section class="card card--front">
  <div class="front__rays" role="img" aria-label="Faint radiating brand decoration"></div>

  <div class="brand-name">CLEARWAY<span class="brand-name__sub">SERVICES</span></div>

  <div class="person">
    <p class="person__name">DANIEL REED</p>
    <p class="person__title">Manager</p>
  </div>

  <ul class="contacts">
    <li>
      <svg viewBox="0 0 16 16" aria-hidden="true"><path fill="#fff" d="M3.5 1.5l2.3 2.6-1.2 1.8c.8 1.8 2.2 3.2 4 4l1.8-1.2 2.6 2.3-1.3 2.3C6.4 13.3 2.7 9.6 1.2 4.2z"/></svg>
      555-018-4372
    </li>
    <li>
      <svg viewBox="0 0 16 16" aria-hidden="true"><rect x="1" y="3" width="14" height="10" fill="#fff"/><path d="M1 3l7 6 7-6" fill="none" stroke="#0a4e93" stroke-width="1.4"/></svg>
      hello@clearwaymail.com
    </li>
    <li>
      <svg viewBox="0 0 16 16" aria-hidden="true"><circle cx="8" cy="8" r="7" fill="#fff"/><circle cx="8" cy="8" r="3" fill="none" stroke="#0a4e93" stroke-width="1.4"/></svg>
      www.clearwayservices.com
    </li>
  </ul>

  <p class="address">Your address, city<br>state, ZIP 0000</p>

  <div class="front__edge"><span class="front__edge-white"></span><span class="front__edge-sky"></span></div>
</section>

<section class="card card--back">
  <div class="back__brand">CLEARWAY<span>SERVICES</span></div>
  <p class="back__license">Licensed &amp; Insured: PA392617</p>
  <div class="services">
    <p class="services__lead">We offer the following services:</p>
    <p>• Deck Repair and Maintenance</p>
    <p>• Deck Cleaning and Staining/Painting • Power Washing/House Washing</p>
    <p>• Landscape Lighting Installation • Christmas Lighting Installation</p>
  </div>
  <div class="tagline-band"></div>
  <p class="tagline">The Steadfast Touch</p>
</section>

</body>
</html>
```